Innovative coffee bean bag design for roasters

We need a design which can be printed on a coffee bean bag but which could also work on a sticker of similar size. We're after quirky, geeky, playful and innovative. Something that will stand out and communicate the character of our business. It should be eye catching and draw the customer in for a closer look.
Thematically, think organic and earthy.
It needs an element which can be changed for different coffee origins and roast profiles, so the main design will remain the same but with a feature which changes to help the customer know what they're looking at and will make them smile.
Approximate dimensions we need are 15cm by 12cm, with the 15cm being the vertical height of the bag image. (The image will be viewed in portrait). This is the main print area - however, if you have a great idea for a full bag image (approximately 23cm by 13cm), feel free to submit this too, we're interested in all ideas.
There is an image attached of a white partially see-through bag which we are considering using, so keep this in mind when designing.
We will need our logo including - see attached image.
Finally, we need space for the information about the coffee, such as origin, roast profile, flavour notes - see attached image for an example of the information (not necessarily a stylistic indicator). Please suggest fonts etc.

Target Market(s)

coffee roasters

Requirements
Must have
• Must say under the logo coffee roasters( Tiny Kettle Organic Coffee Roasters )
Nice to have
• Unique symbol, shapes, scientific.

```html
<!DOCTYPE html>
<html lang="en">
<head>
<meta charset="utf-8">
<title>Tiny Kettle Organic Coffee Roasters – Colombia Label</title>
<link rel="stylesheet" href="https://fonts.googleapis.com/css2?family=Libre+Baskerville:wght@400;700&family=Great+Vibes&family=Arimo:wght@700&display=swap">
<style>
  :root {
    --forest: #1d4f47;
    --cream: #f7f5f3;
    --bean-tone: #e6ddd6;
    --roast-brown: #9a5a34;
    --paper: #ffffff;
    --canvas: #ffffff;
  }
  html, body {
    margin: 0;
    padding: 0;
    width: 1200px;
    height: 1200px;
    overflow: hidden;
    background: var(--canvas);
  }
  .label {
    position: absolute;
    left: 187px;
    top: 80px;
    width: 825px;
    height: 1040px;
    overflow: hidden;
    background: var(--forest);
  }
  .label-art {
    position: absolute;
    inset: 0;
    width: 825px;
    height: 1040px;
  }
  .brand-name {
    position: absolute;
    left: 302px;
    top: 306px;
    width: 220px;
    text-align: center;
    font-family: "Libre Baskerville", serif;
    font-size: 26px;
    line-height: 1.15;
    color: var(--forest);
    margin: 0;
  }
  .roaster-line {
    position: absolute;
    left: 0;
    width: 825px;
    text-align: center;
    color: var(--paper);
    margin: 0;
  }
  .roaster-name {
    top: 490px;
    font-family: "Libre Baskerville", serif;
    font-size: 36px;
  }
  .roaster-script {
    top: 540px;
    font-family: "Great Vibes", cursive;
    font-size: 112px;
    line-height: 1.2;
  }
  .coffee-ticket {
    position: absolute;
    left: 111px;
    top: 729px;
    width: 597px;
    height: 220px;
    box-sizing: border-box;
    border: 3px solid var(--forest);
    color: var(--forest);
    font-family: "Libre Baskerville", serif;
  }
  .roast-profile, .flavour-notes {
    height: 63px;
    display: flex;
    align-items: center;
    justify-content: center;
    font-weight: 700;
    font-size: 30px;
  }
  .roast-profile { border-bottom: 3px solid var(--forest); }
  .flavour-notes { font-weight: 700; font-size: 32px; }
  .origin-row {
    height: 94px;
    display: flex;
    border-bottom: 3px solid var(--forest);
    box-sizing: border-box;
  }
  .origin-name {
    width: 425px;
    display: flex;
    align-items: center;
    justify-content: center;
    font-size: 56px;
    font-weight: 700;
    border-right: 3px solid var(--forest);
  }
  .net-weight {
    flex: 1;
    display: flex;
    align-items: center;
    justify-content: center;
    font-family: "Arimo", sans-serif;
    font-size: 40px;
    font-weight: 700;
  }
</style>
</head>
<body>
  <main class="label">
    <svg class="label-art" viewBox="0 0 825 1040" xmlns="http://www.w3.org/2000/svg">
      <defs>
        <pattern id="ticket-perforation" width="16" height="16" patternUnits="userSpaceOnUse">
          <circle cx="8" cy="8" r="5" fill="var(--forest)"/>
        </pattern>
      </defs>
      <!-- upper panel with bean pattern area -->
      <rect class="bean-field" x="0" y="0" width="825" height="460" fill="var(--bean-tone)" role="img" aria-label="Scattered coffee bean pattern on a light cream ground"/>
      <!-- seal placeholder -->
      <circle class="natural-seal" cx="134" cy="137" r="73" fill="var(--cream)" stroke="var(--forest)" stroke-width="3"/>
      <circle cx="134" cy="137" r="40" fill="none" stroke="var(--forest)" stroke-width="2"/>
      <!-- green dome -->
      <path class="forest-dome" d="M0 440 Q412 200 825 395 L825 1040 L0 1040 Z" fill="var(--forest)"/>
      <!-- brand roundel -->
      <circle cx="412" cy="336" r="152" fill="var(--forest)"/>
      <circle cx="412" cy="336" r="132" fill="var(--paper)"/>
      <circle cx="412" cy="336" r="121" fill="none" stroke="var(--roast-brown)" stroke-width="5"/>
      <!-- origin ticket with perforated edge -->
      <rect x="83" y="710" width="653" height="259" fill="var(--paper)"/>
      <rect x="75" y="710" width="16" height="259" fill="url(#ticket-perforation)"/>
      <rect x="728" y="710" width="16" height="259" fill="url(#ticket-perforation)" transform="translate(0 0)"/>
      <rect x="83" y="702" width="653" height="16" fill="url(#ticket-perforation)"/>
      <rect x="83" y="961" width="653" height="16" fill="url(#ticket-perforation)"/>
    </svg>

    <p class="brand-name">Tiny Kettle</p>

    <h1 class="roaster-line roaster-name">Tiny Kettle Organic</h1>
    <p class="roaster-line roaster-script">Coffee Roasters</p>

    <section class="coffee-ticket">
      <div class="roast-profile">MEDIUM ROAST</div>
      <div class="origin-row">
        <div class="origin-name">COLOMBIA</div>
        <div class="net-weight">500g</div>
      </div>
      <div class="flavour-notes">Caramel &amp; Honey</div>
    </section>
  </main>
</body>
</html>
```